Billboard design for dentist that sees only children

I own a 12' x 25' digital billboard and I need help with billboard design. My wife is a general dentist that only sees children and is very passionate about giving them a quality dental experience . She has a great reputation in town. Obviously with a billboard there can't be a lot of reading. Maybe something that shows safety, love, experience and children. I am completely open to your ideas. In addition I have other businesses that also need billboard design so this could lead to more work. If you go to Maplecovedental.com under the about section you will find more information about the practice and our phone number. Attached is our logo which could be changed and content specs for the digital billboard. Happy Designing!!

Target Market(s)

Parents with children

Colors

Designer to choose colors to be used in the design.

Requirements
Must have
• Must attract attention and be nice to look at.
Nice to have
• Probably should have children in the picture ..... Maybe
Should not have
• If I see something I don't like I will let you know

```html
<!DOCTYPE html>
<html lang="en">
<head>
<meta charset="utf-8">
<title>Maple Cove Dental – Billboard</title>
<link rel="stylesheet" href="https://fonts.googleapis.com/css2?family=Open+Sans:ital,wght@0,400;0,700;1,400;1,700&display=swap">
<style>
  :root {
    --stage: #0b0b0b;
    --panel-top: #f4f8f7;
    --panel-bottom: #98c6bd;
    --brand-green: #2f7d69;
    --tagline-blue: #2f83b8;
    --headline-navy: #1e4b80;
    --phone-bg: #2c6a5b;
    --phone-text: #ffffff;
    --address: #2a2f33;
    --arc-dark: #141a4a;
    --arc-bright: #2b8fd6;
    --photo-light: #efe6dc;
    --photo-mid: #e2c39c;
    --photo-warm: #d9a98a;
  }
  * { box-sizing: border-box; margin: 0; padding: 0; }
  html, body { width: 1200px; height: 1200px; overflow: hidden; background: var(--stage); }
  .canvas { position: relative; width: 1200px; height: 1200px; }
  .billboard {
    position: absolute; left: 40px; top: 332px; width: 1120px; height: 536px;
    background: linear-gradient(180deg, var(--panel-top) 0%, #d6e9e5 45%, var(--panel-bottom) 100%);
    overflow: hidden;
    font-family: "Open Sans", sans-serif;
  }
  .photo-side { position: absolute; inset: 0; width: 100%; height: 100%; }
  .brand { position: absolute; left: 58px; top: 52px; display: flex; align-items: center; gap: 12px; }
  .brand-dot { width: 46px; height: 46px; border-radius: 50%; background: var(--brand-green); }
  .brand-name { font-size: 40px; font-weight: 400; color: var(--brand-green); line-height: 1; letter-spacing: 0.5px; }
  .brand-tagline {
    position: absolute; left: 280px; top: 104px;
    font-size: 19px; font-style: italic; color: var(--tagline-blue);
  }
  .headline {
    position: absolute; left: 40px; width: 520px; top: 160px;
    text-align: center; color: var(--headline-navy);
    font-size: 58px; font-weight: 700; line-height: 66px; letter-spacing: -0.5px;
  }
  .phone {
    position: absolute; left: 106px; top: 378px; width: 388px; height: 70px;
    background: var(--phone-bg); color: var(--phone-text);
    display: flex; align-items: center; justify-content: center;
    font-size: 46px; font-weight: 700; font-style: italic; letter-spacing: 2px;
  }
  .address {
    position: absolute; left: 40px; width: 520px; top: 466px; text-align: center;
    font-size: 26px; font-style: italic; color: var(--address); letter-spacing: 0.5px;
  }
</style>
</head>
<body>
<main class="canvas">
  <section class="billboard">
    <svg class="photo-side" viewBox="0 0 1120 536" preserveAspectRatio="none">
      <defs>
        <linearGradient id="arcGradient" x1="0" y1="0" x2="0" y2="1">
          <stop offset="0" stop-color="var(--arc-dark)"/>
          <stop offset="0.5" stop-color="var(--arc-bright)"/>
          <stop offset="1" stop-color="var(--arc-dark)"/>
        </linearGradient>
        <radialGradient id="photoGradient" cx="0.55" cy="0.5" r="0.7">
          <stop offset="0" stop-color="var(--photo-warm)"/>
          <stop offset="0.55" stop-color="var(--photo-mid)"/>
          <stop offset="1" stop-color="var(--photo-light)"/>
        </radialGradient>
      </defs>
      <path class="accent-arc" d="M690 0 L712 0 Q560 250 640 536 L600 536 Q530 250 690 0 Z" fill="url(#arcGradient)"/>
      <path class="photo-area" role="img" aria-label="Photo of a smiling young girl with a missing front tooth, pointing at her smile"
            d="M712 0 L1120 0 L1120 536 L640 536 Q560 250 712 0 Z" fill="url(#photoGradient)"/>
    </svg>

    <div class="brand">
      <span class="brand-dot"></span>
      <span class="brand-name">Maple Cove Dental</span>
    </div>
    <p class="brand-tagline">general dentistry for children</p>

    <h1 class="headline">Comfortable<br>Dental Care for<br>your Child</h1>

    <p class="phone">555.014.2290</p>
    <p class="address">428 Willow Bend Avenue, Fairhaven</p>
  </section>
</main>
</body>
</html>
```